Brackwell Ponds Trifold About Us Leaflet

I need a A4 Trifold Leaflet Double sided designed with the following information on it:
Logo
Awards
Pictures - Please find on our website www.brackwellponds-example.co.uk or www.facebook.com/brackwellponds
Contact Information
Welcome Text
Events
Ideal for Text
Fishing Text
Camping Text
Map

Target Market(s)

This is almost a paper version of our website.

```html
<!DOCTYPE html>
<html lang="en">
<head>
<meta charset="utf-8">
<title>Brackwell Ponds – Trifold Leaflet</title>
<link rel="stylesheet" href="https://fonts.googleapis.com/css2?family=Questrial&family=Didact+Gothic&display=swap">
<style>
  :root {
    --backdrop: #878787;
    --paper: #ffffff;
    --green: #7bbf2a;
    --green-deep: #5f9e1e;
    --ink: #1d1d1d;
    --ink-soft: #2a2a2a;
    --logo-grey: #6b6b6b;
  }
  * { box-sizing: border-box; margin: 0; padding: 0; }
  html, body {
    width: 1200px; height: 900px; overflow: hidden;
    background: var(--backdrop);
    font-family: "Didact Gothic", "Questrial", sans-serif;
    color: var(--ink);
  }
  .leaflet {
    position: absolute; left: 172px; top: 114px;
    width: 877px; height: 648px;
    background: var(--paper);
    box-shadow: 2px 3px 6px rgba(0,0,0,.45);
    overflow: hidden;
  }
  .leaflet__shapes { position: absolute; inset: 0; }

  .ideal-for { position: absolute; left: 18px; top: 240px; width: 265px; }
  .ideal-for__title {
    display: inline-block; background: var(--paper);
    font-weight: bold; font-size: 13.5px; color: var(--ink);
    padding: 1px 22px 1px 4px; border-radius: 0 8px 8px 0;
    margin-bottom: 8px;
  }
  .ideal-for__item { font-size: 12px; line-height: 13.5px; margin-bottom: 6px; color: var(--ink-soft); white-space: nowrap; }
  .ideal-for__item strong { display: block; color: var(--paper); font-size: 12.5px; margin-bottom: 1px; }

  .contact { position: absolute; left: 291px; width: 294px; top: 338px; text-align: center; }
  .contact__title { font-weight: bold; font-size: 15px; margin-bottom: 18px; font-family: "Questrial", sans-serif; }
  .contact__line { display: flex; justify-content: center; align-items: center; gap: 5px; font-size: 13px; line-height: 20.5px; }
  .contact__line svg { width: 11px; height: 11px; }
  .social { display: flex; justify-content: center; gap: 5px; margin-top: 42px; }
  .social__square { width: 15px; height: 15px; background: var(--ink); border-radius: 3px; }
  .charging { position: absolute; left: 291px; width: 294px; top: 622px; text-align: center; font-size: 12.5px; }

  .brand { position: absolute; left: 638px; top: 22px; width: 200px; }
  .brand__name { font-family: "Questrial", sans-serif; font-size: 25px; color: var(--logo-grey); line-height: 28px; display: flex; align-items: center; gap: 7px; white-space: nowrap; }
  .brand__dot { width: 11px; height: 11px; border-radius: 50%; background: var(--green); flex: none; }
  .brand__type { font-size: 11.5px; color: var(--green-deep); letter-spacing: .4px; margin-top: 1px; white-space: nowrap; }
  .brand__address { font-size: 7px; color: var(--logo-grey); margin-top: 5px; white-space: nowrap; }
  .brand__tel { font-size: 7px; color: var(--green-deep); text-align: right; }

  .haven { position: absolute; right: 16px; top: 477px; width: 150px; text-align: right; font-size: 13px; line-height: 14.6px; color: var(--ink); }
  .haven em { font-style: normal; font-weight: bold; color: var(--green-deep); }
</style>
</head>
<body>
<div class="leaflet">
  <svg class="leaflet__shapes" width="877" height="648" viewBox="0 0 877 648">
    <defs>
      <linearGradient id="silver" x1="0" x2="1" y1="0" y2="0">
        <stop offset="0" stop-color="#8d8d8d"/>
        <stop offset=".5" stop-color="#f4f4f4"/>
        <stop offset="1" stop-color="#9c9c9c"/>
      </linearGradient>
      <linearGradient id="greenBand" x1="0" x2="1" y1="0" y2="1">
        <stop offset="0" stop-color="#6fb21f"/>
        <stop offset=".55" stop-color="#a8dc45"/>
        <stop offset="1" stop-color="#7ec02c"/>
      </linearGradient>
      <linearGradient id="dawn" x1="0" x2="0" y1="0" y2="1">
        <stop offset="0" stop-color="#8a8fa3"/>
        <stop offset=".3" stop-color="#e9a55e"/>
        <stop offset=".42" stop-color="#c9b4a4"/>
        <stop offset=".6" stop-color="#6e6a6a"/>
        <stop offset="1" stop-color="#2d2b2a"/>
      </linearGradient>
      <linearGradient id="pets" x1="0" x2="1" y1="0" y2="1">
        <stop offset="0" stop-color="#a8a8a6"/>
        <stop offset="1" stop-color="#7f7c78"/>
      </linearGradient>
      <linearGradient id="songbird" x1="0" x2="1" y1="0" y2="0">
        <stop offset="0" stop-color="#b9bfc6"/>
        <stop offset=".5" stop-color="#d9dde2"/>
        <stop offset="1" stop-color="#cfd3d9"/>
      </linearGradient>
    </defs>

    <rect class="panel-middle" x="291" y="0" width="294" height="648" fill="url(#silver)"/>
    <path class="panel-left-band" d="M0,70 C60,140 170,230 291,238 V648 H0 Z" fill="url(#greenBand)"/>

    <path class="wave-edge" d="M0,84 C60,155 170,250 290,247 C400,252 520,212 585,152" fill="none" stroke="#ffffff" stroke-width="8"/>
    <path class="photo-dawn" role="img" aria-label="Photo: frosty field and fence at sunrise"
          d="M0,0 H585 V150 C520,210 400,250 290,245 C170,240 60,150 0,80 Z" fill="url(#dawn)"/>

    <path class="photo-pets" role="img" aria-label="Photo: two small dogs carrying a ball"
          d="M0,425 C70,400 160,395 210,425 C265,460 291,560 291,610 V648 H0 Z"
          fill="url(#pets)" stroke="#ffffff" stroke-width="6"/>

    <rect class="panel-right" x="585" y="0" width="292" height="648" fill="#ffffff"/>
    <path class="photo-bird-edge" d="M700,120 C805,112 872,172 855,262 C835,370 755,522 628,648"
          fill="none" stroke="var(--green)" stroke-width="6"/>
    <path class="photo-bird" role="img" aria-label="Photo: small songbird perched on a branch"
          d="M585,165 C620,135 690,122 750,124 C830,130 860,190 845,260 C825,360 740,520 612,648 H585 Z"
          fill="url(#songbird)"/>
  </svg>

  <div class="brand">
    <div class="brand__name"><span>Brackwell Ponds</span><span class="brand__dot"></span></div>
    <div class="brand__type">CARAVAN AND CAMPING PARK</div>
    <div class="brand__address">Ashmere • Langmoor &nbsp;&nbsp; Somerset • TA99 0ZZ</div>
    <div class="brand__tel">Tel: 01632 960811</div>
  </div>

  <section class="ideal-for">
    <h2 class="ideal-for__title">Brackwell Ponds is ideal for</h2>
    <p class="ideal-for__item"><strong>Walking –</strong>The Wenmere Trail is 220mtrs from the<br>campsite</p>
    <p class="ideal-for__item"><strong>Cycling –</strong>Somerset is cris crossed with cycle paths</p>
    <p class="ideal-for__item"><strong>Bird watching –</strong>Over 70 species on site(NBWS<br>survey) and there are lots of NBWS sites locally</p>
  </section>

  <section class="contact">
    <h2 class="contact__title">Contact Us:</h2>
    <p class="contact__line"><svg viewBox="0 0 12 12"><path d="M3 1l2 2-1 1.5c.6 1.4 1.6 2.4 3 3L8.5 6.5l2 2-1.5 2C5 10 2 7 1.5 3z" fill="none" stroke="#1d1d1d" stroke-width="1.1"/></svg>01632 960811</p>
    <p class="contact__line"><svg viewBox="0 0 12 12"><path d="M3 1l2 2-1 1.5c.6 1.4 1.6 2.4 3 3L8.5 6.5l2 2-1.5 2C5 10 2 7 1.5 3z" fill="none" stroke="#1d1d1d" stroke-width="1.1"/></svg>07700900042</p>
    <p class="contact__line"><svg viewBox="0 0 12 12"><circle cx="6" cy="6" r="5" fill="none" stroke="#1d1d1d"/><ellipse cx="6" cy="6" rx="2.2" ry="5" fill="none" stroke="#1d1d1d"/><path d="M1 6h10" stroke="#1d1d1d"/></svg>www.brackwellponds-example.co.uk</p>
    <p class="contact__line"><svg viewBox="0 0 12 12"><rect x="0.5" y="2" width="11" height="8" fill="#1d1d1d"/><path d="M1 2.5l5 4 5-4" fill="none" stroke="#fff"/></svg>info@brackwellponds-example.co.uk</p>
    <div class="social"><span class="social__square"></span><span class="social__square"></span><span class="social__square"></span></div>
  </section>

  <p class="charging">Electric car charging point is available</p>

  <p class="haven">A haven<br>of <em>peace,</em><br><em>quiet</em> and<br><em>relaxation</em>. So<br>relax, soak up the<br>silence and live life<br>at a gentler pace...</p>
</div>
</body>
</html>
```